Cafe Sol Verde needs a new look for their new menu

Built on the banks of the Kwalemba River in Mozambique Africa, Cafe Sol Verde needs a new look for their menu.

This is our restaurant's website and facebook page for reference.
www.cafesolverde.co.za
https://www.facebook.com/cafesolverdemoza

I would like a disposable menu printed in a newspaper style. Either an A2 or A3 size (think A3 may be a little too small) Would like English on the one side and Portuguese on the other side.

Here are some guidelines on what we expect on our new menu.
• Black and white print with maybe a splash of colour. Feel free to experiment (particularly in the social media vector images)
• Design and layout
• The size could be either A3 or A2 whichever is recommended and more effective
• If you could follow this basic layout. Each department must have its own block – like in a newspaper. i.e. bits and bites, main meals, information desserts etc…
• Social media logos – Follow us on Instagram, Facebook, Trip advisor,
• Café Sol Verde logo
• Games and random facts, I’m trying to go for a fun interactive menu
• Look and feel, elegant, fun, hand drawn, 50’s & 60’s, slightly sexy… maybe a splash of colour… red

Please feel free to contact me with anything you don’t understand, I’m sure with my stunted design jargon, I have left loads out…
Updates

Hi Everyone, Thank you for your designs. I have unfortunately not found anything that really grabs my eye. Thank you kindly for your efforts and take care :)

Target Market(s)

Multi national
Multi racial

Industry/Entity Type

Hospitality

Requirements
Must have
• Halal symbol
• veg symbol
• Easy to follow
Nice to have
• SOMETHING DIFFERENT! :)

```html
<!DOCTYPE html>
<html lang="en">
<head>
<meta charset="utf-8">
<title>Cafe Sol Verde – Drinks Menu</title>
<link href="https://fonts.googleapis.com/css2?family=Parisienne&family=Roboto+Condensed:wght@400;700&family=Oswald:wght@500&display=swap" rel="stylesheet">
<style>
:root{
  --ink:#1a1a1a;
  --paper:#ffffff;
  --muted:#555;
  --rule:#999;
  --accent:#b5121b;
  --wheat-a:#d9c7a0;
  --wheat-b:#f3ebda;
}
*{box-sizing:border-box;margin:0;padding:0}
html,body{width:849px;height:1200px;overflow:hidden;background:var(--paper)}
body{font-family:"Roboto Condensed",sans-serif;color:var(--ink);font-size:8.5px;line-height:1.3;position:relative}
.menu-header{position:absolute;left:0;top:0;width:849px;height:70px;border-bottom:1.5px solid var(--ink)}
.title-script{font-family:"Parisienne",cursive;font-weight:400;color:var(--ink)}
.menu-header .section-title{position:absolute;left:20px;top:6px;font-size:44px}
.menu-header .contact{position:absolute;left:330px;top:12px;text-align:center;font-family:"Oswald",sans-serif;font-size:10px;letter-spacing:.4px;line-height:1.5}
.menu-header .brand{position:absolute;right:24px;top:14px;display:flex;gap:8px;align-items:center}
.badge{width:34px;height:34px;border:1.5px solid var(--ink);border-radius:50%;flex:none}
.brand-name{font-family:"Roboto Condensed",sans-serif;font-weight:700;font-size:12px}
.column{position:absolute;top:80px;bottom:40px}
.col-left{left:18px;width:252px}
.col-mid{left:288px;width:268px;border-left:1px solid var(--rule);border-right:1px solid var(--rule);padding:0 12px}
.col-right{left:572px;width:258px;display:flex;flex-direction:column;justify-content:space-between}
.subhead{font-family:"Oswald",sans-serif;font-size:10px;letter-spacing:1px;text-transform:uppercase;text-align:center;border-top:1px solid var(--ink);border-bottom:1px solid var(--ink);padding:1px 0;margin-bottom:4px}
.block-title{font-size:28px;line-height:1;margin:7px 0 3px}
.block-title.center{text-align:center}
.price-list{list-style:none}
.price-list li{display:flex;justify-content:space-between;gap:4px;border-bottom:1px dotted var(--rule);padding:1.3px 0;text-transform:uppercase}
.price-list li span:last-child{white-space:nowrap}
.price-list .desc{display:block;text-transform:none;color:var(--muted);font-size:7.4px}
.price-list.plain li{text-transform:none}
.accent{color:var(--accent)}
.wheat-art{height:56px;margin:6px 0;background:linear-gradient(90deg,var(--wheat-b),var(--wheat-a),var(--wheat-b))}
.extra-box{border:1.5px solid var(--ink);padding:6px 8px;margin-top:8px}
.extra-box h3{font-family:"Oswald",sans-serif;font-size:12px;text-align:center;letter-spacing:1px;margin-bottom:3px}
.extra-box ul{list-style:none;text-align:center;text-transform:uppercase}
.wines-mark{display:flex;align-items:center;justify-content:center;gap:8px;margin:2px 0 6px}
.wines-mark .title-script{font-size:30px}
.facts h2{font-family:"Oswald",sans-serif;font-size:11px;text-align:center;letter-spacing:1px;margin:6px 0 4px}
.facts ul{list-style:none;font-size:8.2px;line-height:1.35}
.facts li{margin-bottom:5px;padding-left:9px;position:relative}
.facts li::before{content:"";position:absolute;left:0;top:4px;width:4px;height:4px;background:var(--accent);border-radius:50%}
.notice-row{display:flex;gap:6px;margin-top:8px}
.notice{border:1.5px solid var(--ink);padding:6px;font-size:7.8px;line-height:1.4;flex:1}
.notice-badge{width:58px;height:58px;border:2px solid var(--ink);border-radius:50%;flex:none;align-self:center}
.menu-footer{position:absolute;left:18px;right:18px;bottom:10px;border-top:1.5px solid var(--ink);padding-top:4px;font-size:7px;text-align:center}
</style>
</head>
<body>
<header class="menu-header">
  <h1 class="title-script section-title">Spirits</h1>
  <div class="contact">www.cafesolverde.co.za<br>facebook.com/cafesolverdemoza</div>
  <div class="brand"><span class="badge"></span><span class="brand-name">Cafe Sol Verde</span></div>
</header>

<section class="column col-left">
  <div class="subhead">Whisky or Whiskey</div>
  <ul class="price-list">
    <li><span>Glen Harrow Black</span><span>45.00</span></li>
    <li><span>Glen Harrow Red</span><span>30.00</span></li>
    <li><span>Glen Harrow Gold</span><span>60.00</span></li>
    <li><span>Glen Harrow Blue</span><span>150.00</span></li>
    <li><span>Glen Harrow Double Black</span><span>55.00</span></li>
    <li><span>Kilrowan</span><span>32.00</span></li>
    <li><span>Kilrowan Select</span><span>40.00</span></li>
    <li><span>Tall Oak No. 7</span><span>38.00</span></li>
    <li><span>Tall Oak Honey</span><span>38.00</span></li>
    <li><span>Crown Vale 12yr</span><span>48.00</span></li>
    <li><span>Crown Vale 18yr</span><span>85.00</span></li>
    <li><span>Ardmoor Rare</span><span>28.00</span></li>
    <li><span>Bellhaven</span><span>26.00</span></li>
    <li><span>Bellhaven Special Reserve</span><span>34.00</span></li>
    <li><span>Glen Sorra 12yr</span><span>52.00</span></li>
    <li><span>Glen Sorra 15yr</span><span>65.00</span></li>
    <li><span>Highland Fold 10yr</span><span>50.00</span></li>
    <li><span>Three Stags Bourbon</span><span>36.00</span></li>
    <li><span>Old Mill Rye</span><span>34.00</span></li>
    <li><span>Cask Hollow Single Malt</span><span>58.00</span></li>
  </ul>
  <h2 class="title-script block-title">Rum</h2>
  <ul class="price-list">
    <li><span>Admiral Teague Spiced</span><span>28.00</span></li>
    <li><span>Admiral Teague Dark</span><span>28.00</span></li>
    <li><span>Isla Blanca White</span><span>26.00</span></li>
    <li><span>Isla Blanca Gold</span><span>30.00</span></li>
    <li><span>Red Reef Dark</span><span>24.00</span></li>
    <li><span>Coconut Cove</span><span>26.00</span></li>
  </ul>
  <div class="wheat-art" role="img" aria-label="Hand drawn wheat stalks decoration"></div>
  <h2 class="title-script block-title">Vodka</h2>
  <ul class="price-list">
    <li><span>Volkov</span><span>24.00</span></li>
    <li><span>Nordvik</span><span>30.00</span></li>
    <li><span>Nordvik Citron</span><span>32.00</span></li>
  </ul>
  <h2 class="title-script block-title">Brandy</h2>
  <ul class="price-list">
    <li><span>Klipvale</span><span>24.00</span></li>
    <li><span>Belmont</span><span>24.00</span></li>
    <li><span>Cape Cellar 5yr</span><span>30.00</span></li>
    <li><span>Cape Cellar 10yr</span><span>45.00</span></li>
  </ul>
  <h2 class="title-script block-title">Cocktails <span class="accent" style="font-family:'Oswald',sans-serif;font-size:10px">all 85.00</span></h2>
  <ul class="price-list plain">
    <li><span><b>Blue Lagoon</b><span class="desc">vodka, blue curaçao, lemonade</span></span><span>85.00</span></li>
    <li><span><b>Sex on the Beach</b><span class="desc">vodka, peach schnapps, orange, cranberry</span></span><span>85.00</span></li>
    <li><span><b>Caipiroska</b><span class="desc">vodka, lime, sugar, crushed ice</span></span><span>85.00</span></li>
    <li><span><b>Long Island</b><span class="desc">vodka, gin, rum, tequila, triple sec, cola</span></span><span>95.00</span></li>
    <li><span><b>Margarita</b><span class="desc">tequila, triple sec, lime, salt rim</span></span><span>85.00</span></li>
    <li><span><b>Piña Colada</b><span class="desc">white rum, coconut cream, pineapple</span></span><span>85.00</span></li>
    <li><span><b>Alabama Slammer</b><span class="desc">whisky, sloe gin, amaretto, orange</span></span><span>85.00</span></li>
  </ul>
  <h2 class="title-script block-title">Ciders</h2>
  <ul class="price-list">
    <li><span>Marula Dry</span><span>30.00</span></li>
    <li><span>Orchard Gold</span><span>30.00</span></li>
    <li><span>Bellaria</span><span>28.00</span></li>
  </ul>
</section>

<section class="column col-mid">
  <h2 class="title-script block-title center">Shots</h2>
  <ul class="price-list plain">
    <li><span>Tequila</span><span>25.00</span></li>
    <li><span>Sambuca</span><span>25.00</span></li>
    <li><span>Hunterkraut</span><span>30.00</span></li>
    <li><span><b>Jelly Tot</b><span class="desc">vodka, sour apple, grenadine</span></span><span>30.00</span></li>
    <li><span><b>Fire Truck</b><span class="desc">Hunterkraut &amp; cinnamon liqueur</span></span><span>35.00</span></li>
    <li><span><b>Springbok</b><span class="desc">peppermint liqueur &amp; Marulina</span></span><span>30.00</span></li>
    <li><span><b>Fuzzy Worm</b><span class="desc">tequila, peach schnapps &amp; orange</span></span><span>30.00</span></li>
    <li><span><b>Flaming Sambuca</b><span class="desc">lit at the table with coffee beans</span></span><span>35.00</span></li>
    <li><span><b>Slippery Nipple</b><span class="desc">sambuca &amp; Brennan's Cream</span></span><span>30.00</span></li>
    <li><span><b>Sidewinder</b><span class="desc">tequila, cinnamon &amp; lime</span></span><span>30.00</span></li>
    <li><span><b>Blow Job</b><span class="desc">Cafetal, cream liqueur, whipped cream</span></span><span>35.00</span></li>
  </ul>
  <h2 class="title-script block-title center">Sherry, Aperitifs &amp; Cognac</h2>
  <ul class="price-list">
    <li><span>Sweet Sherry</span><span>20.00</span></li>
    <li><span>Dry Sherry</span><span>20.00</span></li>
    <li><span>Port</span><span>22.00</span></li>
    <li><span>Vermouth Rosso</span><span>22.00</span></li>
    <li><span>Cognac VS</span><span>60.00</span></li>
  </ul>
  <h2 class="title-script block-title center">Hot beverages</h2>
  <ul class="price-list plain">
    <li><span>Espresso</span><span>20.00</span></li>
    <li><span>Double Espresso</span><span>28.00</span></li>
    <li><span>Cappuccino</span><span>28.00</span></li>
    <li><span>Café Latte</span><span>30.00</span></li>
    <li><span>Filter Coffee</span><span>22.00</span></li>
    <li><span>Hot Chocolate</span><span>30.00</span></li>
    <li><span>Rooibos / Ceylon Tea</span><span>18.00</span></li>
    <li><span>Irish Coffee – Kilrowan</span><span>55.00</span></li>
    <li><span>Coffee Liqueur Coffee – Cafetal</span><span>55.00</span></li>
    <li><span>Cream Coffee – Brennan's Cream</span><span>55.00</span></li>
    <li><span>Nutty Coffee – Avellino</span><span>55.00</span></li>
  </ul>
  <h2 class="title-script block-title center">Milkshakes</h2>
  <ul class="price-list plain">
    <li><span>Vanilla</span><span>35.00</span></li>
    <li><span>Chocolate</span><span>35.00</span></li>
    <li><span>Strawberry</span><span>35.00</span></li>
    <li><span>Bubblegum</span><span>35.00</span></li>
    <li><span>Coffee</span><span>38.00</span></li>
  </ul>
  <h2 class="title-script block-title center">Dom Pedro</h2>
  <ul class="price-list plain">
    <li><span>Irish – Kilrowan</span><span>55.00</span></li>
    <li><span>Scotch – Glen Harrow</span><span>55.00</span></li>
    <li><span>Cream – Brennan's Cream</span><span>55.00</span></li>
    <li><span>Coffee – Cafetal</span><span>55.00</span></li>
    <li><span>Marula – Marulina</span><span>55.00</span></li>
    <li><span>Hazelnut – Avellino</span><span>55.00</span></li>
  </ul>
  <div class="extra-box">
    <h3>EXTRA SERVICES</h3>
    <ul>
      <li>Corkage per bottle 40.00</li>
      <li>Cake service 50.00</li>
      <li>Private function bookings</li>
      <li>River boat cruises</li>
      <li>Fishing trips</li>
      <li>Airport transfers</li>
    </ul>
  </div>
</section>

<section class="column col-right">
  <div class="wines-block">
    <div class="wines-mark"><span class="badge"></span><span class="title-script">Wines</span></div>
    <div class="subhead">Please ask your server for the current wine list</div>
  </div>
  <div class="facts">
    <h2>FUN FACTS</h2>
    <ul>
      <li>The most expensive bottle of whisky ever sold at auction fetched more than a million dollars.</li>
      <li>Whisky is spelt without an "e" in Scotland and Canada, and with an "e" in Ireland and America.</li>
      <li>Cafe Sol Verde sits on the banks of the Kwalemba River – keep an eye out for hippos while you sip.</li>
      <li>The word "vodka" comes from the Slavic word for water, meaning "little water".</li>
      <li>Rum was once used as currency in early colonial trade across the Atlantic.</li>
      <li>A standard bottle of wine holds roughly six glasses – or one good conversation.</li>
      <li>Coffee beans are actually the seeds of a bright red cherry-like fruit.</li>
      <li>The margarita is said to have been invented for a dancer who was allergic to every spirit except tequila.</li>
      <li>Tequila can only be made from blue agave grown in specific regions of Mexico.</li>
      <li>The piña colada became the official drink of Puerto Rico in 1978.</li>
      <li>Champagne bubbles rise in neat lines from tiny flaws in the glass.</li>
      <li>The oldest known recipe for beer is almost four thousand years old.</li>
      <li>Cognac must be aged for at least two years in French oak barrels.</li>
      <li>Milkshakes were first made with eggs and whisky as a tonic.</li>
      <li>Dom Pedro is a South African favourite – ice cream blended with a liqueur of your choice.</li>
      <li>Sambuca is often served with three coffee beans for health, wealth and happiness.</li>
      <li>Hippos can hold their breath for up to five minutes under the river.</li>
      <li>The Kwalemba River sunset is best enjoyed between 17h30 and 18h15.</li>
    </ul>
  </div>
  <div class="notices">
    <div class="notice-row">
      <div class="notice">Please note that management reserves the right to refuse service. No under 18s will be served alcohol. Prices include VAT and may change without notice. A 10% service charge is added to tables of eight or more. Lost property is kept for one week only. Management is not responsible for any loss or damage to personal belongings.</div>
    </div>
    <div class="notice-row">
      <div class="notice">We offer a selection of halal and vegetarian dishes. Please ask your server for details and look for the symbols on our food menu. Kindly inform us of any allergies before ordering.</div>
      <span class="notice-badge"></span>
    </div>
  </div>
</section>

<footer class="menu-footer">Kitchen closes 22h00 – Friday &amp; Saturday 22h30 &nbsp;•&nbsp; Pizza oven opens 17h00 &nbsp;•&nbsp; Ladies night every Wednesday &nbsp;•&nbsp; Follow us for specials and events</footer>
</body>
</html>
```